Gutschein für Onlineshop DIN A Lang
Zielgruppe
Wir betreiben unter www.feldkiste-online.example einen Onlineshop für Armee- und Outdoorbekleidung sowie Ausrüstung. Für eine Paketbeilage benötigen wir einen Gutschein
Aufgabenstellung
Erstellung eines Gutscheins im DIN A Lang Format (Kuvert) mit Vorder- und Rückseite im CI der Webseite. Logo kann gerne zur Verfügung gestellt werden.
Gutscheincode, Wert und Laufzeit wird noch mitgeteilt.

```html
<!DOCTYPE html>
<html lang="de">
<head>
<meta charset="utf-8">
<title>Feldkiste – Gutschein DIN lang</title>
<link rel="stylesheet" href="https://fonts.googleapis.com/css2?family=Stardos+Stencil:wght@700&family=Arimo:wght@400;700&display=swap">
<style>
  :root {
    --page-bg: #ecebe8;
    --olive-light: #9aa86a;
    --olive-dark: #4b5236;
    --khaki: #8a7450;
    --pale-green: #c9d39a;
    --white: #ffffff;
    --ink: #2b2b24;
    --logo-green: #4b5236;
  }
  * { margin: 0; padding: 0; box-sizing: border-box; }
  html, body { width: 1200px; height: 1200px; overflow: hidden; background: var(--page-bg); }
  body { position: relative; font-family: "Arimo", Arial, sans-serif; color: var(--ink); }

  .voucher {
    position: absolute; left: 184px; width: 842px; height: 412px; overflow: hidden;
    background: var(--khaki);
  }
  .voucher--front { top: 168px; }
  .voucher--back { top: 646px; }

  .torn-band { position: absolute; left: 0; width: 100%; }
  .torn-band--top { top: 0; height: 60px; }
  .torn-band--bottom { bottom: 0; height: 70px; }

  .photo { position: absolute; }
  .front-photo {
    left: 0; top: 24px; width: 842px; height: 340px;
    background: linear-gradient(115deg, #55603c 0%, #b9a27a 28%, #c9ae80 45%, #3b3d4a 62%, #6d7048 80%, #4c5a38 100%);
  }
  .back-photo {
    left: 278px; top: 20px; width: 564px; height: 340px;
    background: linear-gradient(180deg, #3d5478 0%, #8da0b4 40%, #e5d6b0 68%, #e3a653 82%, #6a5440 100%);
  }

  .brand-panel {
    position: absolute; left: 78px; top: 10px; width: 168px; height: 402px;
    background: var(--white); padding: 42px 14px 20px 14px;
  }
  .brand-name {
    font-family: "Arimo", Arial, sans-serif; font-weight: 700; color: var(--logo-green);
    font-size: 30px; letter-spacing: -0.5px; display: flex; align-items: center; gap: 8px;
  }
  .brand-name .mark { width: 14px; height: 14px; background: var(--olive-light); display: inline-block; }
  .brand-copy { position: absolute; left: 14px; top: 236px; width: 145px; font-size: 12px; line-height: 1.3; }
  .brand-copy p + p { margin-top: 14px; }
  .brand-url { position: absolute; left: 14px; bottom: 18px; width: 145px; font-size: 11.5px; line-height: 1.3; font-weight: 700; }

  .stencil { font-family: "Stardos Stencil", "Courier New", serif; font-weight: 700; color: var(--white); }
  .title-band {
    position: absolute; left: 382px; top: 100px; width: 460px; height: 112px;
    background: var(--olive-light); transform: rotate(-3deg); transform-origin: left bottom;
    box-shadow: 6px 8px 0 rgba(40,40,20,0.55);
    display: flex; align-items: center; padding-left: 26px; font-size: 78px; letter-spacing: -2px;
  }
  .value-band {
    position: absolute; left: 610px; top: 198px; width: 232px; height: 92px;
    background: var(--olive-light); box-shadow: -6px 8px 0 rgba(40,40,20,0.55);
    display: flex; align-items: center; padding-left: 34px; font-size: 80px; letter-spacing: -2px;
  }

  .code-panel {
    position: absolute; left: 0; top: 34px; width: 278px; height: 322px;
    background: var(--olive-dark); padding: 40px 22px 0 38px; color: var(--white);
  }
  .code-value { font-size: 96px; line-height: 0.9; letter-spacing: -3px; }
  .code-title { font-size: 39px; line-height: 1; margin-top: 8px; letter-spacing: -2px; white-space: nowrap; }
  .code-label { font-size: 11px; margin-top: 12px; }
  .code-box {
    margin-top: 5px; width: 216px; height: 34px; background: var(--pale-green);
    color: var(--olive-dark); font-size: 26px; font-weight: 700; padding-left: 24px; line-height: 34px;
  }
  .code-terms { margin-top: 12px; width: 216px; font-size: 10.5px; line-height: 1.3; text-align: justify; }

  .logo-box {
    position: absolute; left: 638px; top: 0; width: 148px; height: 110px; background: var(--white);
    display: flex; align-items: center; justify-content: center;
  }
  .logo-box .brand-name { font-size: 27px; }

  .benefits { position: absolute; left: 526px; top: 172px; width: 300px; list-style: none; font-size: 12px; font-weight: 700; line-height: 1.3; color: #2c2e2a; }
  .benefits li { position: relative; padding-left: 15px; margin-bottom: 8px; }
  .benefits svg { position: absolute; left: 0; top: 3px; }
  .back-url { position: absolute; right: 22px; bottom: 16px; font-size: 15px; font-weight: 700; color: #1f1c16; }
</style>
</head>
<body>

<section class="voucher voucher--front" aria-label="Gutschein Vorderseite">
  <div class="photo front-photo" role="img" aria-label="Tarnstoff mit Messer in Scheide, Erkennungsmarken und Flecktarn-Ausrüstung"></div>
  <svg class="torn-band torn-band--top" viewBox="0 0 842 60" preserveAspectRatio="none" aria-hidden="true">
    <polygon fill="#7c6848" points="0,0 842,0 842,44 800,40 770,50 720,38 680,46 640,36 600,44 560,34 520,42 480,36 440,46 400,38 360,44 320,34 280,42 240,36 200,44 160,34 120,42 80,36 40,30 0,36"/>
  </svg>
  <svg class="torn-band torn-band--bottom" viewBox="0 0 842 70" preserveAspectRatio="none" aria-hidden="true">
    <polygon fill="#8a7452" points="0,30 40,24 90,34 140,20 200,30 260,18 320,28 380,16 440,30 500,22 560,34 620,24 680,30 740,20 800,26 842,10 842,70 0,70"/>
  </svg>
  <div class="brand-panel">
    <div class="brand-name">Feldkiste <span class="mark"></span></div>
    <div class="brand-copy">
      <p>Einer der ältesten Online-Armee Versender.</p>
      <p>Große Auswahl an Bekleidung &amp; Ausrüstung für Hobby, Freizeit und Beruf.</p>
    </div>
    <div class="brand-url">www.feldkiste-online.example</div>
  </div>
  <div class="title-band stencil">GUTSCHEIN</div>
  <div class="value-band stencil">25 €</div>
</section>

<section class="voucher voucher--back" aria-label="Gutschein Rückseite">
  <div class="photo back-photo" role="img" aria-label="Zwei Wanderer mit Rucksäcken auf einem Felsen vor Sonnenuntergang"></div>
  <svg class="torn-band torn-band--top" viewBox="0 0 842 60" preserveAspectRatio="none" aria-hidden="true">
    <polygon fill="#7c6848" points="0,0 842,0 842,34 800,28 760,40 720,30 680,38 640,26 600,34 560,28 520,40 480,30 440,36 400,26 360,34 320,24 280,32 240,30 200,40 160,32 120,44 80,36 40,42 0,36"/>
  </svg>
  <svg class="torn-band torn-band--bottom" viewBox="0 0 842 70" preserveAspectRatio="none" aria-hidden="true">
    <polygon fill="#8a7452" points="0,16 40,24 90,14 140,26 200,18 260,30 320,20 380,28 440,22 500,30 560,18 620,26 680,14 740,22 800,6 842,0 842,70 0,70"/>
  </svg>
  <div class="code-panel">
    <div class="code-value stencil">25 €</div>
    <div class="code-title stencil">GUTSCHEIN</div>
    <div class="code-label">Ihr Gutscheincode:</div>
    <div class="code-box">1234567890</div>
    <p class="code-terms">Einmalig einlösbar bis zum XX.XX.2014 unter <b>www.gutschein-muster.example</b>. Nicht mit anderen Aktionen kombinierbar. Nur ein Gutschein pro Kunde.</p>
  </div>
  <div class="logo-box"><div class="brand-name">Feldkiste <span class="mark"></span></div></div>
  <ul class="benefits">
    <li><svg width="10" height="9" viewBox="0 0 10 9"><path d="M1 5 L4 8 L9 1" stroke="#2c2e2a" stroke-width="2" fill="none"/></svg>fast 10 Jahre Bundeswehr-Shop im Internet</li>
    <li><svg width="10" height="9" viewBox="0 0 10 9"><path d="M1 5 L4 8 L9 1" stroke="#2c2e2a" stroke-width="2" fill="none"/></svg>größen Auswahl an Bundeswehrbekleidung, Armeebekleidung sowie umfangreiche Ausrüstung für Arbeit, Hobby und Freizeit</li>
    <li><svg width="10" height="9" viewBox="0 0 10 9"><path d="M1 5 L4 8 L9 1" stroke="#2c2e2a" stroke-width="2" fill="none"/></svg>sofort Lieferung in 24 Stunden</li>
  </ul>
  <div class="back-url">www.feldkiste-online.example</div>
</section>

</body>
</html>
```